Business Card for Wellness Clinic

We need a business card for our new logo. I want it to match the feel of the logo

Target Market(s)

Young professional families looking for holistic health care

Industry/Entity Type

Health And Wellness

Contact Information for Business Card

Our business Name: Brackenfield Health & wellness Centre, our phone #, email address...see attached old business card

Font styles to use
Sans Serif

Colors
33b8a4
cee9f5

Requirements
Must have
• my logo and business name
• Font is "Helvetica Neue LT Std 45 Light" and
• Only for "&" using font "Trajan pro bold"
• Use colors in the logo

```html
<!DOCTYPE html>
<html lang="en">
<head>
<meta charset="utf-8">
<title>Brackenfield Health &amp; wellness Centre – Cards</title>
<link rel="stylesheet" href="https://fonts.googleapis.com/css2?family=Open+Sans:ital,wght@0,300;0,400;0,600;0,700;1,400;1,600&display=swap">
<style>
  :root {
    --teal: #33b8a4;
    --sky: #cee9f5;
    --ink: #1f1f1f;
    --paper: #ffffff;
    --backdrop: #e9ecee;
    --rule: #555555;
  }
  * { margin: 0; padding: 0; box-sizing: border-box; }
  html, body { width: 1200px; height: 1200px; overflow: hidden; }
  body {
    background: var(--backdrop);
    font-family: "Open Sans", Arial, sans-serif;
    color: var(--ink);
    position: relative;
  }
  .card {
    position: absolute;
    width: 560px;
    height: 320px;
    background: var(--paper);
    border-radius: 22px;
    overflow: hidden;
    box-shadow: 0 6px 18px rgba(0,0,0,0.12);
  }
  /* Appointment card */
  .appointment { left: 120px; top: 190px; }
  .brand-name {
    font-weight: 300;
    color: var(--ink);
    text-transform: uppercase;
    letter-spacing: 0.2em;
    line-height: 1.35;
  }
  .appointment .brand-name {
    position: absolute;
    left: 36px; top: 34px;
    font-size: 19px;
    width: 340px;
  }
  .brand-mark {
    position: absolute;
    right: 40px; top: 104px;
    width: 150px; height: 150px;
    background: var(--teal);
    border-radius: 18px;
  }
  .fields {
    position: absolute;
    left: 36px; top: 122px;
    width: 310px;
    list-style: none;
  }
  .fields li {
    display: flex;
    align-items: flex-end;
    height: 40px;
    font-style: italic;
    font-weight: 600;
    font-size: 17px;
  }
  .fields li .line {
    flex: 1;
    border-bottom: 1px solid var(--rule);
    margin-left: 6px;
    margin-bottom: 5px;
  }
  .notice {
    position: absolute;
    left: 36px; top: 252px;
    width: 340px;
    font-style: italic;
    font-size: 13px;
    line-height: 1.45;
  }
  /* Business card */
  .business { left: 520px; top: 670px; }
  .business .swoosh { position: absolute; inset: 0; }
  .person {
    position: absolute;
    left: 34px; top: 30px;
  }
  .person-name {
    color: var(--teal);
    font-weight: 700;
    font-size: 21px;
  }
  .person-title { font-size: 12px; font-weight: 400; margin-top: 1px; }
  .business .brand-name {
    position: absolute;
    right: 30px; top: 110px;
    width: 270px;
    font-size: 15px;
    text-align: right;
  }
  .business .brand-mark {
    right: 130px; top: 70px;
    width: 34px; height: 34px;
    border-radius: 6px;
  }
  .contacts {
    position: absolute;
    left: 30px; top: 186px;
    list-style: none;
    font-size: 13px;
  }
  .contacts li { display: flex; align-items: center; height: 20px; }
  .contacts svg { width: 14px; height: 14px; margin-right: 10px; flex: none; }
  .address {
    position: absolute;
    left: 30px; top: 260px;
    font-size: 12.5px;
  }
</style>
</head>
<body>

<section class="card appointment" aria-label="Appointment card">
  <p class="brand-name">Brackenfield Health &amp; wellness Centre</p>
  <div class="brand-mark" aria-hidden="true"></div>
  <ul class="fields">
    <li>Date:<span class="line"></span></li>
    <li>Time:<span class="line"></span></li>
    <li>For:<span class="line"></span></li>
  </ul>
  <p class="notice">If you are unable to keep your appointment, please provide at least 2 business days notice or full visit fees will apply.</p>
</section>

<section class="card business" aria-label="Business card">
  <svg class="swoosh" viewBox="0 0 560 320" width="560" height="320" aria-hidden="true">
    <path d="M0,132 C250,140 460,210 552,320 L560,320 L560,316 C470,200 255,125 0,118 Z" fill="var(--teal)"/>
    <path d="M0,150 C245,158 455,225 545,320 L0,320 Z" fill="var(--sky)"/>
  </svg>
  <div class="person">
    <p class="person-name">Dr. Maren Holt, N.D.</p>
    <p class="person-title">Naturopathic Doctor</p>
  </div>
  <div class="brand-mark" aria-hidden="true"></div>
  <p class="brand-name">Brackenfield Health &amp; wellness Centre</p>
  <ul class="contacts">
    <li>
      <svg viewBox="0 0 14 14" aria-hidden="true"><rect width="14" height="14" rx="3" fill="var(--teal)"/><rect x="4.5" y="2.5" width="5" height="9" rx="1" fill="none" stroke="#fff" stroke-width="1.2"/></svg>
      613-555-0142
    </li>
    <li>
      <svg viewBox="0 0 14 14" aria-hidden="true"><rect width="14" height="14" rx="3" fill="var(--teal)"/><rect x="3" y="4" width="8" height="6" fill="none" stroke="#fff" stroke-width="1.1"/><path d="M3,4 L7,7.5 L11,4" fill="none" stroke="#fff" stroke-width="1.1"/></svg>
      mholt@brackenfieldnaturo.ca
    </li>
    <li>
      <svg viewBox="0 0 14 14" aria-hidden="true"><rect width="14" height="14" rx="3" fill="var(--teal)"/><circle cx="7" cy="7" r="4" fill="none" stroke="#fff" stroke-width="1.1"/><path d="M3,7 H11 M7,3 V11" stroke="#fff" stroke-width="1"/></svg>
      www.brackenfieldnaturo.ca
    </li>
  </ul>
  <p class="address">48 Larkspur Ave. E, Suite 210, Ottawa, ON K1A 5X9</p>
</section>

</body>
</html>
```